Ardenwell Building and Property Services needs a business card design

We need a business card design for our building and property services business. We already have a logo we just need a creative design and layout on a business card. Emphasis on clean, modern, professional.
Our client targets are mainly body corporates, building managers, construction managers.
We are a building services company that lean more to structural repair of buildings, through concrete rectification and carbon fibre strengthening.
We also refurbish facades, rendering, painting etc
We target higher end body corporates in prestigious locations, hence why we'd like our cards to reflect professionalism, strength, efficiency

Target Market(s)

body corporates, building managers, construction managers

Industry/Entity Type

Construction

Contact Information for Business Card

Ardenwell is the main word, with 'Building and Property Services' underneath.
Level 17, 82 Harlow Street
MERRIDALE
Melbourne
Vic 3094
T: 9518 2736
Duncan Ferris - Director
dunardenwell@mailbox-example.com

Requirements
Must have
• Stand out on the back of the card- strong/ bold, company logo
• All of the contact details written above
Should not have
• I'd like the card to stand out, especially on the back. Id like the company logo to be prominent, although feel free to be creative around it. But remain clean and professional

```html
<!DOCTYPE html>
<html lang="en">
<head>
<meta charset="utf-8">
<title>Ardenwell Building and Property Services – Business Card</title>
<link rel="stylesheet" href="https://fonts.googleapis.com/css2?family=Roboto+Condensed:wght@700&family=Open+Sans:wght@400&display=swap">
<style>
  :root {
    --stage: #5a5c5b;
    --card: #030303;
    --brand-blue: #1a8fd6;
    --text-light: #e2e2e2;
    --text-muted: #c9c9c9;
    --divider: #5a5a5a;
  }
  * { box-sizing: border-box; margin: 0; padding: 0; }
  html, body {
    width: 1200px;
    height: 1200px;
    overflow: hidden;
    background: var(--stage);
  }
  .canvas {
    width: 1200px;
    height: 1200px;
    display: flex;
    flex-direction: column;
    align-items: center;
    justify-content: center;
    gap: 40px;
  }
  .card {
    width: 900px;
    height: 530px;
    background: var(--card);
    position: relative;
  }

  /* Back of card */
  .card-back {
    display: flex;
    align-items: center;
    justify-content: center;
  }
  .brand-mark {
    display: flex;
    align-items: center;
    gap: 22px;
    font-family: "Open Sans", sans-serif;
    font-weight: 400;
    color: var(--brand-blue);
    font-size: 72px;
    letter-spacing: 6px;
    text-transform: uppercase;
  }
  .brand-square {
    width: 46px;
    height: 46px;
    background: var(--brand-blue);
  }

  /* Front of card */
  .card-front {
    display: flex;
    align-items: center;
  }
  .brand-block {
    width: 400px;
    display: flex;
    flex-direction: column;
    align-items: center;
    gap: 14px;
    font-family: "Open Sans", sans-serif;
    font-weight: 400;
    color: var(--brand-blue);
  }
  .brand-block .brand-square { width: 34px; height: 34px; }
  .brand-name {
    font-size: 46px;
    letter-spacing: 4px;
    text-transform: uppercase;
  }
  .brand-tagline {
    font-size: 14px;
    letter-spacing: 2px;
    text-transform: uppercase;
    color: var(--text-light);
  }
  .divider {
    width: 1px;
    height: 290px;
    background: var(--divider);
  }
  .contact-block {
    padding-left: 44px;
    font-family: "Open Sans", sans-serif;
    color: var(--text-light);
  }
  .person-name {
    font-family: "Roboto Condensed", sans-serif;
    font-weight: 700;
    font-size: 32px;
    color: var(--brand-blue);
  }
  .person-role {
    font-size: 22px;
    color: var(--text-muted);
    margin-top: 2px;
  }
  .address {
    font-size: 20px;
    line-height: 1.45;
    margin-top: 52px;
    color: var(--text-muted);
  }
  .contact-line {
    display: flex;
    align-items: center;
    gap: 26px;
    margin-top: 22px;
    font-size: 24px;
  }
  .contact-line.phone { margin-top: 34px; font-size: 28px; }
  .icon { width: 34px; height: 30px; flex-shrink: 0; }
</style>
</head>
<body>
<main class="canvas">
  <section class="card card-back" aria-label="Card back">
    <div class="brand-mark">
      <span class="brand-square"></span>
      <span>Ardenwell</span>
    </div>
  </section>

  <section class="card card-front" aria-label="Card front">
    <div class="brand-block">
      <span class="brand-square"></span>
      <span class="brand-name">Ardenwell</span>
      <span class="brand-tagline">Building and Property Services</span>
    </div>
    <div class="divider"></div>
    <div class="contact-block">
      <p class="person-name">Duncan Ferris</p>
      <p class="person-role">Director</p>
      <p class="address">Level 17, 82 Harlow Street<br>MERRIDALE Melbourne&nbsp; Vic 3094</p>
      <p class="contact-line phone">
        <svg class="icon" viewBox="0 0 34 30" aria-hidden="true">
          <path d="M2 9 Q17 -1 32 9 L29 13 L24 11 L24 7 Q17 4 10 7 L10 11 L5 13 Z" fill="var(--brand-blue)"/>
          <path d="M8 13 L26 13 L31 27 L3 27 Z" fill="var(--brand-blue)"/>
          <circle cx="17" cy="20" r="4" fill="var(--card)"/>
        </svg>
        <span>9518 2736</span>
      </p>
      <p class="contact-line email">
        <svg class="icon" viewBox="0 0 34 30" aria-hidden="true">
          <rect x="1" y="4" width="32" height="22" fill="var(--brand-blue)"/>
          <path d="M2 5 L17 17 L32 5 M2 25 L13 14 M32 25 L21 14" stroke="var(--card)" stroke-width="2" fill="none"/>
        </svg>
        <span>dunardenwell@mailbox-example.com</span>
      </p>
    </div>
  </section>
</main>
</body>
</html>
```